Flyer to Promote Membership in a Trade Association

UPDATE: I am looking for something modern and clean. NO CLIP ART. Not flashy. Just professional and modern. For everyone looking at our current flyer, we don't like it. That's why we aer looking for a new one. So please don't replicate it or use it as inspiration.

I need a flyer to promote membership in the Durable Residence Backers League. It can (probably should) be 2-sided. The content is attached as well as our logo and brand guidelines.

```html
<!DOCTYPE html>
<html lang="en">
<head>
<meta charset="utf-8">
<title>Durable Residence Backers League — Membership</title>
<link href="https://fonts.googleapis.com/css2?family=Open+Sans:wght@600;700;800&family=Encode+Sans+Condensed:wght@300;400&family=Source+Serif+4:wght@700;800&display=swap" rel="stylesheet">
<style>
:root{
  --orange:#f37e33;
  --ink:#111;
  --grey-text:#555;
  --page-bg:#d3d9dc;
  --card:#fff;
  --band-grey:#efe9e9;
  --overlay:rgba(55,60,66,.82);
  --rule:#bdbdbd;
}
*{margin:0;padding:0;box-sizing:border-box}
html,body{width:927px;height:1200px;overflow:hidden;background:var(--page-bg)}
.flyer{position:absolute;left:32px;top:41px;width:864px;height:1118px;background:var(--card);overflow:hidden;font-family:'Open Sans',sans-serif;color:var(--ink)}
.hero-photo{position:absolute;left:0;top:0;width:864px;height:320px;background:linear-gradient(100deg,#8d8a86 0%,#6e6a66 25%,#c9c7c3 50%,#e7e5e2 70%,#b9b6b2 100%)}
.hero-panel{position:absolute;left:0;top:95px;width:446px;height:187px;background:var(--overlay)}
.hero-kicker{position:absolute;left:74px;top:24px;font-weight:700;font-size:31px;color:var(--orange);letter-spacing:.5px}
.hero-title{position:absolute;left:62px;top:52px;font-family:'Source Serif 4',serif;font-weight:800;font-size:68px;color:#fff;letter-spacing:-1px;line-height:1}
.hero-sub{position:absolute;left:71px;top:135px;font-family:'Encode Sans Condensed',sans-serif;font-weight:300;font-size:12.5px;color:#fff}
.band{position:absolute;height:47px}
.band svg{position:absolute;left:0;top:0}
.band span{position:absolute;top:11px;font-weight:600;font-size:18.5px;color:#fff;letter-spacing:.3px}
.benefits{position:absolute;left:62px;top:378px;width:353px}
.benefit{border-bottom:1px solid var(--rule);padding:7px 0 4px}
.benefit h3{font-weight:600;font-size:14.5px;line-height:19px}
.benefit h3 em{font-style:normal;color:var(--orange);margin-left:6px}
.benefit p{font-family:'Encode Sans Condensed',sans-serif;font-weight:300;font-size:12.6px;line-height:18px;color:var(--grey-text)}
.tiers{position:absolute;left:503px;width:296px}
.tier{font-weight:600;font-size:14.5px;padding:6px 0 5px;border-bottom:1px solid var(--rule)}
.tier.last{border-bottom:1.5px solid var(--ink)}
.price{border-bottom:1px solid var(--rule);padding:3px 0 1px;color:var(--orange);font-weight:700;font-size:29px;line-height:38px}
.price small{font-size:16px}
.price i{font-style:normal;font-family:'Source Serif 4',serif;font-size:11.5px;color:#444;margin-left:5px}
.cta{position:absolute;left:503px;top:752px}
.cta-line1{font-weight:800;font-size:47px;line-height:54px;letter-spacing:.5px}
.cta-line2{font-weight:800;font-size:42px;line-height:54px;color:var(--orange);margin-left:-3px}
.cta-tag{font-family:'Encode Sans Condensed',sans-serif;font-weight:300;font-size:13.5px;color:var(--grey-text);margin-top:2px}
.roster{position:absolute;left:0;top:919px;width:864px;height:134px;background:var(--band-grey);text-align:center}
.roster h2{font-weight:700;font-size:18px;margin-top:28px}
.roster p{font-family:'Encode Sans Condensed',sans-serif;font-weight:300;font-size:9px;line-height:13.5px;color:var(--grey-text);width:660px;margin:7px auto 0}
.footer{position:absolute;left:0;top:1053px;width:864px;height:65px;background:var(--orange);text-align:center;color:#fff;font-weight:700;font-size:18px;line-height:65px;letter-spacing:.5px}
</style>
</head>
<body>
<main class="flyer">
  <div class="hero-photo" role="img" aria-label="Photo of colleagues reviewing documents together in a bright office"></div>
  <div class="hero-panel">
    <div class="hero-kicker">UNLIMITED</div>
    <div class="hero-title">ACCESS</div>
    <div class="hero-sub">One membership, your entire team can participate in DRBL activities.</div>
  </div>

  <div class="band" style="left:0;top:320px;width:426px">
    <svg width="426" height="47"><polygon points="0,0 426,0 399,47 0,47" fill="#f37e33"/></svg>
    <span style="left:62px">MEMBER BENEFITS</span>
  </div>
  <div class="band" style="left:454px;top:320px;width:410px">
    <svg width="410" height="47"><polygon points="26,0 410,0 410,47 0,47" fill="#f37e33"/></svg>
    <span style="left:49px">INVESTOR MEMBERS</span>
  </div>

  <section class="benefits">
    <div class="benefit"><h3>Members-Only Conferences</h3><p>Two annual in-person meetings. Spring Meeting: investors-only for candid peer conversations. Fall Summit: full ecosystem gathering with syndicators and brokers</p></div>
    <div class="benefit"><h3>Investor-Only Forums</h3><p>Exclusive meetings and webinars for investors only, enabling candid conversations and meaningful collaboration.</p></div>
    <div class="benefit"><h3>Peer-to-Peer Meetups</h3><p>Find your peers—underwriters, asset managers, credit officers and more—with our meetups.</p></div>
    <div class="benefit"><h3>Live &amp; On-Demand Webinars</h3><p>Free monthly Third Thursday webinars covering Year 15 issues, secondary transactions, securitizing developer fees and other emerging topics.</p></div>
    <div class="benefit"><h3>Searchable Member Directory</h3><p>Find underwriters, asset managers, and credit officers—searchable by role, firm type, and investment approach.</p></div>
    <div class="benefit"><h3>Shape Industry Standards<em>[INVESTOR ONLY]</em></h3><p>DRBL’s underwriting and asset management standards are adopted industry-wide. Influence them through our committees.</p></div>
    <div class="benefit"><h3>Emerging Leaders Program<em>[INVESTOR ONLY]</em></h3><p>Develop your firm’s next-generation leaders through dedicated professional development programming.</p></div>
  </section>

  <section class="tiers" style="top:378px">
    <div class="tier">Bank</div>
    <div class="tier">Insurance Companies</div>
    <div class="tier last">Economic Investors.</div>
    <div class="price">$5,000<small>/year</small><i>(assets ≥ $5B)</i></div>
    <div class="price">$1,000<small>/year</small><i>(assets &lt; $5B)</i></div>
  </section>

  <div class="band" style="left:454px;top:588px;width:410px">
    <svg width="410" height="47"><polygon points="26,0 410,0 410,47 0,47" fill="#f37e33"/></svg>
    <span style="left:63px">AFFILIATE MEMBERS</span>
  </div>

  <section class="tiers" style="top:644px">
    <div class="tier last">Syndicators &amp; Brokers.</div>
    <div class="price">$4,500<small>/year</small></div>
  </section>

  <section class="cta">
    <div class="cta-line1">BECOME A</div>
    <div class="cta-line2">DRBL MEMBER</div>
    <div class="cta-tag">The Only Community Built Exclusively for LIHTC Investors</div>
  </section>

  <section class="roster">
    <h2>OUR INVESTOR MEMBERS</h2>
    <p>Halden Life/Corwell Health • Bright Harbor Bank • Meridian Trust National Bank • Grandview Bank • Corvel Bank • Oakline Financial • Summit One • Ashford Bank • Northvale Trust • Seventh Arch CDC • Lakeside Citizens Bank • Penrose Partners • Keystone Ridge Bank • Whitmore Capital • Prairie Mutual Insurance • Hudson Crest Life • Everly (ALTA) • Crestpoint Real Estate • Southland Affordable Housing • Marisol Bank • Brightcoat Works • Tidewell Bank • Harborton Bank • Clearview Community Capital • Vantora Bank USA • Liberty Crest • Cardinal Bancorp Impact Finance • Redwood Valley Bank.</p>
  </section>

  <footer class="footer">WWW.DRBL.ORG</footer>
</main>
</body>
</html>
```